Veterinary Business cards

Redesign Business Card

Information needed on Card:
Hours: Mon-Fri: 4pm -10PM; Sat- Sun- 10 AM- 5PM
Help@bayfernvet.com
www.bayfernvet.com
555-718-2946
4173 SE 19th Ave. okc, ok 73958
*No appointment necessary*

Optional:
Our tag line is "We're here when you need us" - If it fits on the cards.

```html
<!DOCTYPE html>
<html lang="en">
<head>
<meta charset="utf-8">
<title>Bayfern Urgent Care – Business Card</title>
<link rel="stylesheet" href="https://fonts.googleapis.com/css2?family=Arimo:ital,wght@0,400;0,700;1,700&display=swap">
<style>
  :root {
    --navy: #1c3f6c;
    --orange: #e07b1c;
    --paper: #f6f6f5;
    --ink: #1c3f6c;
    --backdrop: #2b2b2b;
  }
  * { box-sizing: border-box; margin: 0; padding: 0; }
  html, body { width: 1200px; height: 900px; overflow: hidden; }
  body {
    background: var(--backdrop);
    font-family: "Arimo", Arial, sans-serif;
    display: flex;
    flex-direction: column;
    align-items: center;
    justify-content: center;
    gap: 60px;
  }
  .card {
    position: relative;
    width: 560px;
    height: 320px;
    border-radius: 22px;
    overflow: hidden;
  }
  /* front */
  .card-front { background: var(--paper); }
  .brand {
    position: absolute;
    left: 36px; top: 92px;
    width: 230px;
    display: flex;
    align-items: center;
    gap: 12px;
  }
  .brand-mark {
    width: 26px; height: 26px;
    border-radius: 50%;
    background: var(--orange);
    flex: none;
  }
  .brand-name {
    color: var(--navy);
    font-weight: 400;
    font-size: 26px;
    line-height: 1.1;
    letter-spacing: 0.5px;
  }
  .divider {
    position: absolute;
    left: 290px; top: 40px;
    width: 1px; height: 170px;
    background: #9aa3ad;
  }
  .details {
    position: absolute;
    left: 310px; top: 34px;
    color: var(--ink);
    font-size: 13.5px;
    line-height: 1.35;
  }
  .hours-label { color: var(--orange); font-weight: 700; font-size: 14px; }
  .hours { margin-left: 10px; margin-bottom: 10px; }
  .contact { list-style: none; margin-left: 18px; }
  .contact li { display: flex; align-items: center; gap: 7px; }
  .contact svg { width: 13px; height: 13px; flex: none; }
  .address { margin-left: 20px; margin-top: 12px; }
  .tagline-band {
    position: absolute;
    left: 0; right: 0; top: 222px;
    height: 52px;
    background: var(--navy);
    display: flex;
    align-items: center;
    justify-content: center;
  }
  .tagline {
    color: var(--orange);
    font-weight: 700;
    font-style: italic;
    font-size: 21px;
    letter-spacing: 1px;
    text-transform: uppercase;
  }
  /* back */
  .card-back {
    background: var(--navy);
    display: flex;
    align-items: center;
    justify-content: center;
    gap: 14px;
  }
  .card-back .brand-name { color: #ffffff; font-size: 34px; }
  .card-back .brand-mark { width: 32px; height: 32px; }
</style>
</head>
<body>
  <section class="card card-front">
    <div class="brand">
      <span class="brand-mark"></span>
      <span class="brand-name">Bayfern<br>Urgent Care</span>
    </div>
    <div class="divider"></div>
    <div class="details">
      <p class="hours-label">Hours:</p>
      <p class="hours">Mon-Fri: 4pm -10PM;<br>Sat- Sun- 10 AM- 5PM</p>
      <ul class="contact">
        <li>
          <svg viewBox="0 0 16 16" aria-hidden="true"><path fill="var(--orange)" d="M3.5 1.5l2.5 0 1 3.5-1.6 1.2a8 8 0 0 0 4.4 4.4L11 9l3.5 1v2.5c0 1-1 2-2 2C6.5 14.5 1.5 9.5 1.5 3.5c0-1 1-2 2-2z"/></svg>
          555-718-2946
        </li>
        <li>
          <svg viewBox="0 0 16 16" aria-hidden="true"><rect x="1" y="3" width="14" height="10" fill="var(--orange)"/><path d="M1 3l7 6 7-6" fill="none" stroke="#fff" stroke-width="1.2"/></svg>
          Help@bayfernvet.com
        </li>
        <li>
          <svg viewBox="0 0 16 16" aria-hidden="true"><g fill="none" stroke="var(--orange)" stroke-width="1.4"><circle cx="8" cy="8" r="6.5"/><ellipse cx="8" cy="8" rx="2.8" ry="6.5"/><path d="M1.5 8h13M3 4.5h10M3 11.5h10"/></g></svg>
          www.bayfernvet.com
        </li>
      </ul>
      <p class="address">4173 SE 19th Ave. okc, ok 73958</p>
    </div>
    <div class="tagline-band">
      <p class="tagline">We're here when you need us</p>
    </div>
  </section>

  <section class="card card-back">
    <span class="brand-mark"></span>
    <span class="brand-name">Bayfern<br>Urgent Care</span>
  </section>
</body>
</html>
```